Carpentry and Building Business Card

I'm looking for a business card that is minimalistic and that incorporates the theme of my Velmor logo.
On one side I'd like the VELMOR logo with my details on the other side.
Double sided with curved edges

Target Market(s)

Construction / renovation
Adults

Industry/Entity Type

Tradesman

Contact Information for Business Card

Logo on one side, details on the other

Colors

Designer to choose only greyscale colors for use in the design.

Requirements
Must have
• Nilo Petrakis
VELMOR CONSTRUCT
Carpentry & Building Services
0481236574
Velmorconstruct@brixmail.com
Lic No. 718263D
Nice to have
• Fb and insta icons. @velmorconstruct
Should not have
• No hammer or tool icons please.

No address line.

```html
<!DOCTYPE html>
<html lang="en">
<head>
<meta charset="utf-8">
<title>Velmor Construct – Business Card</title>
<link rel="stylesheet" href="https://fonts.googleapis.com/css2?family=Poppins:wght@300;400;500;700&display=swap">
<style>
  :root {
    --page: #f3f3f2;
    --card-light: #3d3d3d;
    --card-mid: #222222;
    --card-dark: #0c0c0c;
    --text: #ffffff;
    --rule: #d9d9d9;
    --accent: #e3a032;
  }
  * { margin: 0; padding: 0; box-sizing: border-box; }
  html, body { width: 1200px; height: 1200px; overflow: hidden; }
  body {
    background: var(--page);
    font-family: "Poppins", Arial, sans-serif;
    color: var(--text);
    position: relative;
  }
  .card {
    position: absolute;
    left: 237px;
    width: 736px;
    height: 430px;
    border-radius: 52px;
    overflow: hidden;
  }
  .card--front { top: 148px; }
  .card--back { top: 609px; }
  .card__backdrop {
    position: absolute;
    inset: 0;
    background: linear-gradient(170deg, var(--card-light) 0%, var(--card-mid) 55%, var(--card-dark) 100%);
  }

  .brand {
    position: absolute;
    left: 42px;
    top: 93px;
    display: flex;
    align-items: center;
    gap: 30px;
  }
  .brand__mark {
    width: 108px;
    height: 120px;
    border: 3px solid var(--accent);
  }
  .brand__name {
    font-weight: 500;
    font-size: 62px;
    letter-spacing: 0.28em;
    line-height: 1;
  }

  .details { position: absolute; left: 30px; top: 36px; }
  .details__name {
    font-weight: 700;
    font-size: 39px;
    line-height: 1;
  }
  .details__company {
    font-weight: 300;
    font-size: 39px;
    line-height: 1;
    margin-top: 2px;
  }
  .details__tagline {
    font-weight: 300;
    font-size: 25px;
    line-height: 1.2;
    margin-top: 12px;
    letter-spacing: 0.01em;
  }
  .details__rule {
    position: absolute;
    left: 30px;
    top: 173px;
    width: 416px;
    height: 2px;
    background: var(--rule);
  }
  .contact { position: absolute; left: 30px; top: 196px; list-style: none; }
  .contact__item {
    display: flex;
    align-items: center;
    height: 33px;
    margin-bottom: 2px;
    font-weight: 300;
    font-size: 21px;
  }
  .contact__item:nth-child(3) { margin-top: 4px; }
  .contact__icon { width: 16px; height: 16px; margin-right: 20px; flex: none; }
  .contact__dot {
    width: 12px; height: 12px; border-radius: 50%;
    background: var(--text); margin: 0 24px 0 2px; flex: none;
  }
</style>
</head>
<body>

<section class="card card--front" aria-label="Business card front">
  <div class="card__backdrop" role="img" aria-label="Dark layered curved wave background"></div>
  <div class="brand">
    <span class="brand__mark"></span>
    <span class="brand__name">VELMOR.</span>
  </div>
</section>

<section class="card card--back" aria-label="Business card back">
  <div class="card__backdrop" role="img" aria-label="Dark layered curved wave background"></div>

  <div class="details">
    <h1 class="details__name">NILO PETRAKIS</h1>
    <p class="details__company">VELMOR CONSTRUCT</p>
    <p class="details__tagline">Carpentry &amp; Building Services</p>
  </div>
  <div class="details__rule"></div>

  <ul class="contact">
    <li class="contact__item">
      <svg class="contact__icon" viewBox="0 0 16 16" aria-hidden="true">
        <path d="M3.5 1.5 L6 4.5 L4.6 6.2 C5.4 8 7.5 10.2 9.8 11.4 L11.5 10 L14.5 12.5 L12.8 14.5 C7.5 14 2 8.5 1.5 3.2 Z" fill="#fff"/>
      </svg>
      <span>0481236574</span>
    </li>
    <li class="contact__item">
      <svg class="contact__icon" viewBox="0 0 16 16" aria-hidden="true">
        <rect x="1" y="3.5" width="14" height="9.5" fill="#fff"/>
        <path d="M1 3.5 L8 9 L15 3.5 M1 13 L6 8 M15 13 L10 8" stroke="#1a1a1a" stroke-width="1" fill="none"/>
      </svg>
      <span>Velmorconstruct@brixmail.com</span>
    </li>
    <li class="contact__item">
      <svg class="contact__icon" viewBox="0 0 16 16" aria-hidden="true">
        <rect x="1" y="2.5" width="14" height="11" rx="1" fill="none" stroke="#fff" stroke-width="1.3"/>
        <rect x="3" y="5" width="4" height="4" fill="#fff"/>
        <path d="M8.5 5.5 H13 M8.5 8 H13 M3 11 H13" stroke="#fff" stroke-width="1.2"/>
      </svg>
      <span>Lic No. 718263D</span>
    </li>
    <li class="contact__item">
      <span class="contact__dot"></span>
      <span>@velmorconstruct</span>
    </li>
  </ul>
</section>

</body>
</html>
```